Lucien Marchand

Changes to attached business card: 1. Eliminate borders (black) top and bottom of the existing card. 2- eliminate: Become the reference! 3- adding: www.doublezvoschiffres.ca info@doublezvoschiffres.ca lucienmarchandconseil.com (819) 555-2736 4- black on white

Contact Information for Business Card

voir pièce ci-jointe pour exemple

Requirements
Must have
• black on white
Nice to have
• Very modern ! with punch!

```html
<!DOCTYPE html>
<html lang="fr">
<head>
<meta charset="utf-8">
<title>Lucien Marchand — Carte d'affaires</title>
<link href="https://fonts.googleapis.com/css2?family=Oswald:wght@500;600&display=swap" rel="stylesheet">
<style>
  :root {
    --backdrop: #2a0205;
    --card: #ffffff;
    --gold: #c9a332;
    --ink: #111111;
  }
  * { box-sizing: border-box; margin: 0; padding: 0; }
  html, body {
    width: 1200px; height: 900px; overflow: hidden;
    background: var(--backdrop);
    font-family: "Oswald", "Arial Narrow", sans-serif;
  }
  .card {
    position: absolute; left: 100px; top: 164px;
    width: 1000px; height: 572px;
    background: var(--card);
    box-shadow: 0 20px 50px rgba(0,0,0,.45);
  }
  .brand-mark {
    position: absolute; left: 0; top: 0; width: 330px; height: 100%;
    display: flex; flex-direction: column; align-items: center; justify-content: center; gap: 22px;
  }
  .brand-dot { width: 120px; height: 120px; border-radius: 50%; background: var(--gold); }
  .brand-name {
    color: var(--gold); font-weight: 600; font-size: 30px;
    text-transform: uppercase; letter-spacing: .5px;
  }
  .divider {
    position: absolute; left: 330px; top: 80px;
    width: 3px; height: 412px; background: var(--gold);
  }
  .info { position: absolute; left: 400px; top: 70px; width: 560px; }
  .name {
    color: var(--gold); font-weight: 600; font-size: 64px; line-height: 1;
    text-transform: uppercase; letter-spacing: -.5px;
  }
  .title {
    display: flex; align-items: center; gap: 10px; margin-top: 8px;
    color: var(--ink); font-weight: 600; font-size: 34px; line-height: 1;
  }
  .title::before, .title::after { content: ""; height: 2px; background: var(--ink); }
  .title::before { width: 40px; }
  .title::after { width: 40px; }
  .contacts { margin-top: 56px; display: flex; flex-direction: column; gap: 26px; }
  .contact { display: flex; align-items: center; gap: 22px; }
  .contact-icon {
    flex: none; width: 58px; height: 58px; border-radius: 50%;
    background: var(--gold); display: flex; align-items: center; justify-content: center;
  }
  .contact-icon svg { width: 32px; height: 32px; }
  .contact-lines { color: var(--ink); font-weight: 500; font-size: 24px; line-height: 1.12; }
  .contact-lines.phone { font-size: 32px; }
</style>
</head>
<body>
  <div class="card">
    <div class="brand-mark">
      <span class="brand-dot"></span>
      <span class="brand-name">Lucien Marchand</span>
    </div>
    <div class="divider"></div>
    <div class="info">
      <h1 class="name">Lucien Marchand</h1>
      <p class="title">Consultant - Coach</p>
      <div class="contacts">
        <div class="contact">
          <span class="contact-icon">
            <svg viewBox="0 0 32 32" fill="none" stroke="#fff" stroke-width="2">
              <circle cx="16" cy="16" r="12"/>
              <ellipse cx="16" cy="16" rx="5.5" ry="12"/>
              <line x1="4" y1="16" x2="28" y2="16"/>
              <line x1="6" y1="10" x2="26" y2="10"/>
              <line x1="6" y1="22" x2="26" y2="22"/>
            </svg>
          </span>
          <p class="contact-lines">www.doublezvoschiffres.ca<br>www.lucienmarchandconseil.com</p>
        </div>
        <div class="contact">
          <span class="contact-icon">
            <svg viewBox="0 0 32 32" fill="none" stroke="#fff" stroke-width="2" stroke-linejoin="round">
              <rect x="4" y="8" width="24" height="16"/>
              <polyline points="4,8 16,18 28,8"/>
              <line x1="4" y1="24" x2="13" y2="15.5"/>
              <line x1="28" y1="24" x2="19" y2="15.5"/>
            </svg>
          </span>
          <p class="contact-lines">info@doublezvoschiffres.ca<br>lucienmarchand.conseil@boitemail.ca</p>
        </div>
        <div class="contact">
          <span class="contact-icon">
            <svg viewBox="0 0 32 32" fill="#fff">
              <path d="M10 5c1 0 1.6.6 2 1.5l1.6 3.8c.4.9.1 1.8-.6 2.4l-1.7 1.4c1.2 2.6 3.2 4.6 5.8 5.8l1.4-1.7c.6-.7 1.5-1 2.4-.6l3.8 1.6c.9.4 1.5 1 1.5 2V24c0 1.7-1.3 3-3 3C13.9 27 5 18.1 5 8c0-1.7 1.3-3 3-3z"/>
            </svg>
          </span>
          <p class="contact-lines phone">(819) 555-2736</p>
        </div>
      </div>
    </div>
  </div>
</body>
</html>
```